Business Card Design Project

We need a Business Card for an Mechanical Engineering firm in Singapore. The design should be Modern & Technical looking, yet eye catching.

Our company deals in Cutting Tools & Machine Accessories for the Manufacturing Industries such as Oil & Gas, Aero Space, etc... For more information on our Company, you can either email me or view our website www.valtrion.com.sg.

We are trying to revamp our image to give our consumers a fresh new perspective to our company, so we welcome all ideas.

Industry/Entity Type

Business

Requirements
Must have
• Must incorporate New Company Logo into the card as shown in Uploaded file.

```html
<!DOCTYPE html>
<html lang="en">
<head>
<meta charset="utf-8">
<title>Valtrion Tools – Business Card</title>
<link rel="stylesheet" href="https://fonts.googleapis.com/css2?family=Arimo:wght@400;700&display=swap">
<style>
  :root {
    --stage: #e6e6e6;
    --card-black: #1f1b1b;
    --band-black: #231f1f;
    --brand-red: #8f1c21;
    --brand-red-light: #b3262c;
    --paper: #ffffff;
    --paper-shade: #d9d9d9;
    --ink-light: #ffffff;
    --ink-soft: #e4e4e4;
  }
  * { box-sizing: border-box; margin: 0; padding: 0; }
  html, body {
    width: 1200px; height: 951px; overflow: hidden;
    background: var(--stage);
    font-family: "Arimo", Arial, sans-serif;
  }
  .canvas { position: relative; width: 1200px; height: 951px; }

  .card {
    position: absolute; width: 600px; height: 343px;
    border-radius: 26px; overflow: hidden;
    box-shadow: 0 10px 28px rgba(0,0,0,.25);
  }

  /* Front side */
  .card--front {
    left: 110px; top: 90px;
    background: var(--card-black);
    border-left: 22px solid var(--brand-red);
    border-right: 22px solid var(--brand-red);
    display: flex; flex-direction: column; align-items: center; justify-content: center;
  }
  .brand {
    display: flex; align-items: center; gap: 16px;
    color: var(--ink-light);
  }
  .brand__dot {
    width: 44px; height: 44px; border-radius: 50%;
    background: var(--brand-red-light);
  }
  .brand__name {
    font-weight: 700; font-size: 48px; letter-spacing: 1px;
  }
  .front__web {
    margin-top: 34px; color: var(--ink-soft);
    font-size: 19px; letter-spacing: .5px;
  }

  /* Back side */
  .card--back {
    left: 490px; top: 510px;
    background: linear-gradient(180deg, var(--paper) 0%, var(--paper) 55%, var(--paper-shade) 100%);
  }
  .info-band {
    position: absolute; left: 0; right: 0; top: 116px; height: 172px;
    background: var(--band-black);
    display: flex;
  }
  .identity {
    width: 232px; height: 100%;
    background: linear-gradient(135deg, var(--brand-red-light), var(--brand-red));
    padding: 48px 0 0 26px; color: var(--ink-light);
  }
  .identity__name { font-size: 24px; }
  .identity__role { font-size: 16px; margin-top: 4px; }
  .divider {
    width: 2px; background: #6b6464; margin: 62px 0 62px 20px;
  }
  .contacts {
    list-style: none; color: var(--ink-light);
    font-size: 17px; line-height: 1.2; padding: 14px 0 0 22px;
  }
  .contacts li { display: flex; align-items: center; gap: 10px; }
  .contacts li + li { margin-top: 2px; }
  .contacts .address { align-items: flex-start; margin-bottom: 14px; }
  .contacts svg { width: 16px; height: 16px; flex: none; fill: var(--ink-light); }
</style>
</head>
<body>
<main class="canvas">
  <section class="card card--front" aria-label="Card front">
    <div class="brand">
      <span class="brand__dot"></span>
      <span class="brand__name">VALTRION TOOLS</span>
    </div>
    <p class="front__web">www.valtriontools.com</p>
  </section>

  <section class="card card--back" aria-label="Card back">
    <div class="info-band">
      <div class="identity">
        <p class="identity__name">Marcus Tane</p>
        <p class="identity__role">manager</p>
      </div>
      <span class="divider"></span>
      <ul class="contacts">
        <li class="address">
          <svg viewBox="0 0 16 16"><path d="M8 1 1 7.5h2V15h4v-4h2v4h4V7.5h2z"/></svg>
          <span>1480 Harlow Crest Rd.<br>Dunmore, TX 78114</span>
        </li>
        <li>
          <svg viewBox="0 0 16 16"><path d="M4 1.5 6.5 4 5 6c1 2 3 4 5 5l2-1.5 2.5 2.5-2 2.5C7 14 2 9 1.5 3.5z"/></svg>
          <span>512-555-0142</span>
        </li>
        <li>
          <svg viewBox="0 0 16 16"><rect x="4" y="1" width="8" height="14" rx="1.5"/></svg>
          <span>512-555-0143</span>
        </li>
        <li>
          <svg viewBox="0 0 16 16"><path d="M1 3h14v10H1zM1.5 3.5 8 9l6.5-5.5" stroke="#231f1f" stroke-width="1.2"/></svg>
          <span>info@valtriontools.com</span>
        </li>
        <li>
          <svg viewBox="0 0 16 16"><circle cx="8" cy="8" r="7"/></svg>
          <span>www.valtriontools.com</span>
        </li>
      </ul>
    </div>
  </section>
</main>
</body>
</html>
```